依頼概要
日本語学校のポスターデザインをお願いします。
今年の10月に新規開校します

サイズ:A0、A1、各1
学校情報:http://www.kesu.jp
ポスター使用目的:海外での学生募集説明会、海外教育機関への営業
納品形式:イラレ、jpeg、各1

ポスター内容:
・学校写真、学生寮写真(それぞれ枚数指定なし)
・「日本に留学しよう」のような誘い文句
・その他文章の作成をお願いします
・募集コース:4月期生、10月期生

要望:
・A1をメインで使用します。
・A0はA1を拡大したものでも結構ですし、別にデザインして頂いても結構です。
(報酬は変わらないので、ご了承下さい。すみません。)
・当方イラレを持っていないので、イラレの他に必ずjpeg形式またはofficeソフト形式で納品をお願いします。(photoshopは持ってます)
・シンプルというか、パッと見て分かり易い感じのデザインでお願いしたいですが、デザインの幅を狭めたくない気持ちもあります。
・学費含め費用関連は、載せないで下さい。
・入学案内関連の情報は、「募集コース」以外は載せないで下さい。

写真について:
・場所やアングルの指定などをして頂ければ、頑張って撮影してきます。
(もちろん、素人撮影です)
・10月に新規開校なので、授業風景の写真は用意できません。
・同じ理由で教員やスタッフ、人物の写真は用意ができません。
・花火大会のパーティーや、クリスマスパーティーの写真はあります。

日本語学校とは:(ご存知ない方もいらっしゃるかと思いますので、簡単に)
・生徒は全て外国籍の留学生です。
・日本の大学や大学院、専門学校への進学を目標に日本語学校で約2年、日本語の勉強をします。

当校の特徴:
・利根川の土手沿いに校舎があります。とっても静かです。
・校舎から約100mのところが花火大会の打ち上げ場所です。
・その他添付資料をご参照下さい。

その他:
ロゴのデータを添付しますのでご使用下さい。
学校に関連した文章も添付しておきますので、ご参考まで。
デザインの採用をさせて頂いた後で写真を撮ってきますので、その後に微調整をして納品をお願いします。
なので、納品まで少々時間がかかります。

以上、どうぞよろしくお願い致します。

生徒募集の為の宣伝ポスターを作る予定だったのですが、こちらのデザインは宣伝としての役割だけでなく、一つの絵として完成されていると思いました。空間を華やかに飾ってくれるデザインで、海外の教育機関だけでなく、商業施設にも持ち込み易いと思い、採用をさせて頂きました。

ご提案頂きましたワーカルの皆様。素敵なデザインをご提案頂き、ありがとうございました。期待以上の作品ばかりでスタッフ一同大変悩みました。今後もまたこちらに依頼をすることがあるかと思いますので、またご縁があればと思います。皆様のご発展をお祈り申し上げます。ありがとうございました。

```html
<!DOCTYPE html>
<html lang="ja">
<head>
<meta charset="utf-8">
<title>日本をもっと好きになる。</title>
<link rel="stylesheet" href="https://fonts.googleapis.com/css2?family=Noto+Serif+JP:wght@500;700&family=Noto+Sans+JP:wght@400;700&family=Archivo+Black&display=swap">
<style>
  :root {
    --paper: #ffffff;
    --ink: #111111;
    --navy: #1f2a5c;
    --red: #e60012;
    --grey-box: #e6e6e6;
    --grey-line: #9a9a9a;
    --body-ink: #444444;
  }
  html, body { margin: 0; padding: 0; overflow: hidden; background: var(--paper); }
  .poster {
    position: relative;
    width: 846px; height: 1200px;
    background: var(--paper);
    overflow: hidden;
    font-family: "Noto Sans JP", sans-serif;
  }
  .brand-bar {
    position: absolute; left: 40px; top: 22px;
    height: 44px;
    background: var(--navy);
    display: flex; align-items: center; gap: 8px;
    padding: 0 14px 0 10px; box-sizing: border-box;
  }
  .brand-bar .mark { width: 26px; height: 26px; background: #f2f2f2; flex: none; }
  .brand-bar .name { color: #fff; font-size: 15px; font-weight: 700; letter-spacing: 0.02em; white-space: nowrap; }
  .intro {
    position: absolute; left: 118px; top: 118px; width: 420px;
    font-size: 8.5px; line-height: 1.75; color: var(--body-ink);
    margin: 0; text-align: justify;
  }
  .campus-photo {
    position: absolute; left: 0; top: 268px; width: 846px; height: 622px;
    background: linear-gradient(180deg, #c9d0d8 0%, #a8a9a0 45%, #8b6a4e 75%, #5d4a3c 100%);
  }
  .headline {
    position: absolute; right: 30px; top: 38px; height: 560px;
    writing-mode: vertical-rl;
    font-family: "Noto Serif JP", serif; font-weight: 700;
    font-size: 86px; line-height: 1.12; letter-spacing: 0.02em;
    color: var(--ink); margin: 0;
  }
  .slogan {
    position: absolute; left: 12px; top: 902px;
    font-family: "Archivo Black", sans-serif;
    font-size: 118px; line-height: 1; color: var(--ink);
    letter-spacing: -0.01em; margin: 0; white-space: nowrap;
    display: flex; align-items: center;
  }
  .slogan .heart-o {
    display: inline-block; width: 97px; height: 97px; border-radius: 50%;
    background: var(--red); margin: 0 2px;
  }
  .footer-logo {
    position: absolute; left: 20px; top: 1032px; width: 240px;
    display: flex; flex-direction: column; align-items: center; gap: 10px;
  }
  .footer-logo .mark { width: 100px; height: 100px; background: var(--navy); }
  .footer-logo .name { font-size: 15px; font-weight: 700; color: var(--navy); white-space: nowrap; }
  .info-box {
    position: absolute; left: 270px; top: 1030px; width: 220px; height: 150px;
    background: var(--grey-box);
  }
  .info-box svg { position: absolute; inset: 0; }
  .info-box .label {
    position: absolute; left: 0; right: 0; top: 66px; text-align: center;
    font-size: 10px; color: #555; background: var(--grey-box);
    width: 130px; margin: 0 auto; padding: 2px 0;
  }
  .dorm-photo {
    position: absolute; left: 500px; top: 1030px; width: 346px; height: 150px;
    background: linear-gradient(180deg, #9fb6cc 0%, #c4cbc6 40%, #5f6e57 75%, #4a5a43 100%);
  }
</style>
</head>
<body>
<main class="poster">
  <header class="brand-bar">
    <span class="mark"></span>
    <span class="name">坂東リバーサイド日本語学院</span>
  </header>

  <p class="intro">坂東リバーサイド日本語学院は、川の土手沿いに建つ静かな学び舎です。世界中から集まる留学生が、日本の大学や大学院、専門学校への進学を目指し、約二年間じっくりと日本語を学びます。校舎のすぐそばでは夏の花火大会が開かれ、季節ごとの行事を通して日本の文化や暮らしに触れることができます。落ち着いた環境と温かな仲間に囲まれて、あなたの夢への第一歩を踏み出しましょう。募集コースは四月期生と十月期生です。皆さんのご応募を心よりお待ちしています。</p>

  <div class="campus-photo" role="img" aria-label="校舎前に座って語り合う二人の留学生と背景の校舎の写真"></div>

  <h1 class="headline">日本をもっと<br>好きになる。</h1>

  <p class="slogan">L<span class="heart-o" aria-hidden="true"></span>VE&nbsp;JAPAN</p>

  <div class="footer-logo">
    <span class="mark"></span>
    <span class="name">坂東リバーサイド日本語学院</span>
  </div>

  <div class="info-box">
    <svg width="220" height="150" viewBox="0 0 220 150" aria-hidden="true">
      <rect x="0.5" y="0.5" width="219" height="149" fill="none" stroke="var(--grey-line)"/>
      <line x1="0" y1="0" x2="220" y2="150" stroke="var(--grey-line)"/>
      <line x1="220" y1="0" x2="0" y2="150" stroke="var(--grey-line)"/>
    </svg>
    <p class="label">住所等必要情報記載欄</p>
  </div>

  <div class="dorm-photo" role="img" aria-label="緑に囲まれた学生寮の建物の写真"></div>
</main>
</body>
</html>
```